Palvette International needs a book cover

I am self publishing a book titles entitled, Quiet Threads Through Carrying and Raising. Pressline Yard is ready to do the print, but I did not like their design. I am attaching the picture I want on the front.

Hello all - Thank you all for your beautiful designs.  I am closing this project in 24 hours. I will be making my final selection then.  I apologize for closing earlier than my deadline.  This is my first project and I have learned a lot:)  I will be back with more projects!

```html
<!DOCTYPE html>
<html lang="en">
<head>
<meta charset="utf-8">
<title>Quiet Threads Through Carrying and Raising — Book Cover</title>
<link rel="stylesheet" href="https://fonts.googleapis.com/css2?family=Pinyon+Script&family=Cinzel:wght@400&display=swap">
<style>
  :root {
    --blush: #f3c6da;
    --rose: #e8a9c8;
    --petal: #fbe6f0;
    --lavender: #c7b6ea;
    --lilac: #b3a3e0;
    --mist: #fdf5fa;
    --ink: #141014;
  }
  html, body {
    margin: 0;
    padding: 0;
    width: 1200px;
    height: 933px;
    overflow: hidden;
    background: var(--mist);
  }
  .cover {
    position: relative;
    width: 1200px;
    height: 933px;
    overflow: hidden;
  }
  .cover-photo {
    position: absolute;
    inset: 0;
    background:
      radial-gradient(ellipse 260px 200px at 180px 120px, var(--mist) 0%, rgba(253,245,250,0) 70%),
      radial-gradient(ellipse 340px 260px at 860px 140px, var(--lilac) 0%, rgba(179,163,224,0) 75%),
      radial-gradient(ellipse 260px 300px at 1110px 360px, var(--lavender) 0%, rgba(199,182,234,0) 75%),
      radial-gradient(ellipse 300px 360px at 640px 560px, var(--petal) 0%, rgba(251,230,240,0) 75%),
      radial-gradient(ellipse 500px 300px at 260px 520px, var(--rose) 0%, rgba(232,169,200,0) 75%),
      radial-gradient(ellipse 420px 260px at 980px 760px, var(--rose) 0%, rgba(232,169,200,0) 75%),
      radial-gradient(ellipse 360px 220px at 240px 860px, var(--mist) 0%, rgba(253,245,250,0) 75%),
      linear-gradient(135deg, var(--blush) 0%, var(--petal) 45%, var(--lavender) 100%);
  }
  .spine-title {
    position: absolute;
    left: 560px;
    top: 250px;
    width: 440px;
    transform-origin: 0 0;
    transform: translateX(64px) rotate(90deg);
    font-family: "Pinyon Script", cursive;
    color: var(--ink);
    line-height: 1;
    margin: 0;
  }
  .spine-title .main {
    display: block;
    font-size: 38px;
  }
  .spine-title .sub {
    display: block;
    font-size: 19px;
    padding-left: 22px;
  }
  .front-title {
    position: absolute;
    left: 700px;
    top: 440px;
    width: 490px;
    margin: 0;
    font-family: "Pinyon Script", cursive;
    font-weight: 400;
    color: var(--ink);
    line-height: 1;
  }
  .front-title .line-1 {
    display: block;
    font-size: 84px;
    padding-left: 42px;
  }
  .front-title .line-2 {
    display: block;
    font-size: 44px;
    padding-left: 96px;
    margin-top: -14px;
  }
  .front-title .line-3 {
    display: block;
    font-size: 32px;
    padding-left: 6px;
    margin-top: 2px;
  }
  .author {
    position: absolute;
    left: 712px;
    top: 846px;
    width: 430px;
    margin: 0;
    font-family: "Cinzel", serif;
    font-size: 32px;
    letter-spacing: 1px;
    color: var(--ink);
    white-space: nowrap;
  }
</style>
</head>
<body>
  <main class="cover">
    <div class="cover-photo" role="img" aria-label="Soft pink and lavender photograph of a pregnant mother wearing a baby's-breath flower crown, resting with a young woman and a small child gathered around her belly"></div>

    <p class="spine-title">
      <span class="main">Quiet Threads</span>
      <span class="sub">through Carrying &amp; Raising</span>
    </p>

    <h1 class="front-title">
      <span class="line-1">Quiet</span>
      <span class="line-2">Threads Through</span>
      <span class="line-3">Carrying &amp; Raising</span>
    </h1>

    <p class="author">Lena Marie Halvers</p>
  </main>
</body>
</html>
```